Redesign Login page

I want to redesign my login page to bring my 2 products closer together. I am only looking to redesign one login page, not 2.

For the logo, please make it solid and it can be black or white if helpful. I can also fine tune the logo if you get it close.

Coding

Coded - Design and coding required

Number of Pages Required

1 page

```html
<!DOCTYPE html>
<html lang="en">
<head>
<meta charset="UTF-8">
<title>Velora – Sign In</title>
<link href="https://fonts.googleapis.com/css2?family=Poppins:wght@400;500;700&display=swap" rel="stylesheet">
<style>
  :root {
    --page-bg: #ffffff;
    --card-bg: #a13220;
    --field-bg: #efefef;
    --field-text: #6f6f6f;
    --accent: #9c8a45;
    --white: #ffffff;
  }
  * { box-sizing: border-box; margin: 0; padding: 0; }
  html, body {
    width: 1016px;
    height: 1200px;
    overflow: hidden;
    background: var(--page-bg);
    font-family: "Poppins", sans-serif;
  }
  .login-card {
    position: absolute;
    left: 136px;
    top: 132px;
    width: 744px;
    height: 935px;
    background: var(--card-bg);
    border-radius: 56px;
    box-shadow: 0 6px 30px rgba(0,0,0,0.18);
    color: var(--white);
  }
  .welcome {
    position: absolute;
    top: 62px;
    width: 100%;
    text-align: center;
    font-size: 27px;
    font-weight: 400;
  }
  .brand-name {
    position: absolute;
    top: 130px;
    width: 100%;
    text-align: center;
    font-size: 128px;
    font-weight: 700;
    line-height: 1.2;
    letter-spacing: -2px;
  }
  .field {
    position: absolute;
    left: 38px;
    width: 646px;
    height: 85px;
    border-radius: 43px;
    background: var(--field-bg);
    color: var(--field-text);
    font-size: 20px;
    padding-left: 44px;
  }
  .field-email {
    top: 390px;
    display: flex;
    align-items: center;
  }
  .field-password { top: 502px; }
  .field-password .field-label {
    position: absolute;
    top: 17px;
    left: 44px;
  }
  .field-password .field-value {
    position: absolute;
    top: 38px;
    left: 44px;
    font-size: 22px;
    letter-spacing: -1px;
    font-weight: 700;
  }
  .toggle-visibility {
    position: absolute;
    right: 32px;
    top: 27px;
    width: 36px;
    height: 30px;
  }
  .btn-continue {
    position: absolute;
    top: 614px;
    left: 38px;
    width: 646px;
    height: 85px;
    border-radius: 43px;
    background: var(--accent);
    color: var(--white);
    font-size: 28px;
    font-weight: 500;
    display: flex;
    align-items: center;
    justify-content: center;
  }
  .options-row {
    position: absolute;
    top: 730px;
    left: 56px;
    right: 78px;
    height: 34px;
    display: flex;
    align-items: center;
    justify-content: space-between;
    font-size: 22px;
    font-weight: 500;
  }
  .remember {
    display: flex;
    align-items: center;
    gap: 16px;
  }
  .checkbox {
    width: 29px;
    height: 29px;
    border: 2px solid var(--white);
    border-radius: 5px;
  }
  .text-link {
    border-bottom: 1.5px solid var(--white);
    line-height: 1.15;
  }
  .signup-line {
    position: absolute;
    top: 816px;
    width: 100%;
    text-align: center;
    font-size: 22px;
    font-weight: 500;
  }
</style>
</head>
<body>
  <main class="login-card">
    <p class="welcome">Welcome To</p>
    <h1 class="brand-name">Velora</h1>

    <div class="field field-email">Email</div>

    <div class="field field-password">
      <span class="field-label">Password</span>
      <span class="field-value">•••••••••</span>
      <svg class="toggle-visibility" viewBox="0 0 36 30" fill="none" stroke="#6f6f6f" stroke-width="2.2" stroke-linecap="round">
        <path d="M3 15 C9 6 27 6 33 15 C27 24 9 24 3 15 Z"/>
        <circle cx="18" cy="15" r="5.5"/>
        <line x1="7" y1="27" x2="29" y2="3"/>
      </svg>
    </div>

    <div class="btn-continue">Continue</div>

    <div class="options-row">
      <div class="remember"><span class="checkbox"></span><span>Remember Me</span></div>
      <span class="text-link">Forgot Password?</span>
    </div>

    <p class="signup-line">Don't have an account? <span class="text-link">Sign up</span></p>
  </main>
</body>
</html>
```